Business Card Design Project - IT Company

Kestrafield Information Technology Solutions
We are an Information Technology Company. We provide computer services to commercial companies. We would like a new card full color front and back with bleeding edge.
We have a logo that you can use or if you want to come up with a new logo that is fine too.
Our colors are mostly Maroon and black but be creative.
Sample Information
Brent R Okafor
4812 W Saguaro Ridge Drive
Suite 600
Phoenix, AZ 85016
O: 602.914.2037
C: 602.468.1290
24/7: 888.914.2037
bokafor@kestrafield.example
www.kestrafield.example
Target Market(s)
Business of all sizes
Industry/Entity Type
Computer
Requirements
Must have
- Bleeding edge
full color on both sides

```html
<!DOCTYPE html>
<html lang="en">
<head>
<meta charset="utf-8">
<title>Kestrafield Business Card – Front and Back</title>
<link rel="stylesheet" href="https://fonts.googleapis.com/css2?family=Open+Sans:wght@400;600;700&family=Tinos:wght@400;700&family=Pirata+One&display=swap">
<style>
  :root {
    --stage: #6b6b6b;
    --maroon-deep: #4a0306;
    --maroon: #8e0a10;
    --maroon-bright: #b0141b;
    --swoosh: #151515;
    --paper-light: #f4f4f4;
    --paper-shade: #cfcfcf;
    --ink: #2a2a2a;
    --name-red: #8a1016;
    --ghost: #d9d9d9;
    --white: #ffffff;
    --label: #ffffff;
  }
  * { box-sizing: border-box; margin: 0; padding: 0; }
  html, body { width: 1200px; height: 520px; overflow: hidden; }
  body { background: var(--stage); position: relative; font-family: "Open Sans", Arial, sans-serif; }

  .card {
    position: absolute;
    top: 80px;
    width: 548px;
    height: 324px;
    border-radius: 14px;
    overflow: hidden;
    box-shadow: 0 2px 6px rgba(0,0,0,.35);
  }
  .card--front { left: 32px; }
  .card--back { left: 620px; }

  .card__art { position: absolute; inset: 0; width: 100%; height: 100%; display: block; }

  .brand {
    position: absolute;
    top: 44px;
    left: 0;
    right: 0;
    text-align: center;
    color: var(--white);
  }
  .brand__name {
    font-family: "Open Sans", Arial, sans-serif;
    font-weight: 400;
    font-size: 40px;
    line-height: 1;
    letter-spacing: 1px;
    color: var(--white);
  }
  .brand__tagline {
    font-family: "Tinos", "Times New Roman", serif;
    font-size: 14px;
    margin-top: 6px;
    color: var(--white);
  }

  .contact {
    position: absolute;
    top: 190px;
    left: 0;
    right: 0;
    text-align: center;
    color: var(--ink);
  }
  .contact__name {
    font-family: "Tinos", "Times New Roman", serif;
    font-weight: 700;
    font-size: 21px;
    color: var(--name-red);
    letter-spacing: .5px;
    margin-bottom: 4px;
  }
  .contact__line {
    font-family: "Open Sans", Arial, sans-serif;
    font-weight: 600;
    font-size: 12.5px;
    line-height: 17px;
  }
  .contact__web {
    position: absolute;
    left: 0;
    right: 0;
    top: 284px;
    text-align: center;
    font-family: "Open Sans", Arial, sans-serif;
    font-size: 14px;
    color: var(--ink);
    letter-spacing: .3px;
  }

  .ghost-name {
    position: absolute;
    left: 0;
    right: 0;
    top: 196px;
    text-align: center;
    font-family: "Open Sans", Arial, sans-serif;
    font-weight: 400;
    font-size: 66px;
    line-height: 1;
    color: var(--ghost);
    letter-spacing: 1px;
  }
  .back-web {
    position: absolute;
    left: 0;
    right: 0;
    top: 270px;
    text-align: center;
    font-family: "Open Sans", Arial, sans-serif;
    font-size: 23px;
    color: var(--ink);
    letter-spacing: .5px;
  }

  .side-label {
    position: absolute;
    top: 418px;
    width: 548px;
    text-align: center;
    font-family: "Pirata One", "Times New Roman", serif;
    font-size: 48px;
    color: var(--label);
  }
  .side-label--front { left: 32px; }
  .side-label--back { left: 620px; }
</style>
</head>
<body>

  <section class="card card--front" aria-label="Business card front">
    <svg class="card__art" viewBox="0 0 548 324" preserveAspectRatio="none" aria-hidden="true">
      <defs>
        <radialGradient id="front-red" cx="50%" cy="35%" r="70%">
          <stop offset="0" stop-color="var(--maroon-bright)"/>
          <stop offset=".55" stop-color="var(--maroon)"/>
          <stop offset="1" stop-color="var(--maroon-deep)"/>
        </radialGradient>
        <radialGradient id="front-paper" cx="50%" cy="55%" r="70%">
          <stop offset="0" stop-color="var(--paper-light)"/>
          <stop offset="1" stop-color="var(--paper-shade)"/>
        </radialGradient>
      </defs>
      <rect width="548" height="324" fill="url(#front-red)"/>
      <path d="M0 176 C120 150 300 150 548 162 L548 188 C330 176 150 178 0 206 Z" fill="var(--swoosh)"/>
      <path d="M0 206 C150 178 330 176 548 188 L548 324 L0 324 Z" fill="url(#front-paper)"/>
    </svg>

    <header class="brand">
      <div class="brand__name">KESTRAFIELD</div>
      <div class="brand__tagline">Information Technology Solutions</div>
    </header>

    <address class="contact" style="font-style: normal;">
      <div class="contact__name">Brent R Okafor</div>
      <div class="contact__line">4812 W Saguaro Ridge Drive, Suite 600 Phoenix, AZ 85016</div>
      <div class="contact__line">O: 602.914.2037 | C: 602.468.1290</div>
      <div class="contact__line">24/7: 888.914.2037</div>
    </address>
    <div class="contact__web">www.kestrafield.example | bokafor@kestrafield.example</div>
  </section>

  <section class="card card--back" aria-label="Business card back">
    <svg class="card__art" viewBox="0 0 548 324" preserveAspectRatio="none" aria-hidden="true">
      <defs>
        <radialGradient id="back-red" cx="50%" cy="35%" r="70%">
          <stop offset="0" stop-color="var(--maroon-bright)"/>
          <stop offset=".55" stop-color="var(--maroon)"/>
          <stop offset="1" stop-color="var(--maroon-deep)"/>
        </radialGradient>
        <radialGradient id="back-paper" cx="50%" cy="55%" r="70%">
          <stop offset="0" stop-color="var(--paper-light)"/>
          <stop offset="1" stop-color="var(--paper-shade)"/>
        </radialGradient>
      </defs>
      <rect width="548" height="324" fill="url(#back-red)"/>
      <path d="M0 176 C120 150 300 150 548 162 L548 188 C330 176 150 178 0 206 Z" fill="var(--swoosh)"/>
      <path d="M0 206 C150 178 330 176 548 188 L548 324 L0 324 Z" fill="url(#back-paper)"/>
    </svg>

    <header class="brand">
      <div class="brand__name">KESTRAFIELD</div>
      <div class="brand__tagline">Information Technology Solutions</div>
    </header>

    <div class="ghost-name" aria-hidden="true">KESTRAFIELD</div>
    <div class="back-web">www.kestrafield.example</div>
  </section>

  <div class="side-label side-label--front">Front</div>
  <div class="side-label side-label--back">Back</div>

</body>
</html>
```